Letterhead to Prospective Clients

Create a letterhead (word & canva) that I will use to send letters to prospective clients and also include the Harbourline Estate Group Logo, My Contact Details and Interchangeable "Suburb". Use the same font and colour pallete

Maris Toppel | "Suburb" Specialist - Redlands & Surrounds
Mobile: 0417 862 905
Email: MT@HarbourlineEstateGroup.com.au

```html
<!DOCTYPE html>
<html lang="en">
<head>
<meta charset="utf-8">
<title>Harbourline Estate Group – Letterhead</title>
<link rel="stylesheet" href="https://fonts.googleapis.com/css2?family=Arimo:wght@400;700&family=Figtree:wght@300;400;700&display=swap">
<style>
  :root {
    --backdrop: #edeef0;
    --paper: #ffffff;
    --paper-edge: #dcdde0;
    --navy: #111c3f;
    --sand: #d9a46f;
    --ink: #555555;
    --ink-soft: #5e5e5e;
    --signature: #e6e6e6;
  }
  * { margin: 0; padding: 0; box-sizing: border-box; }
  html, body {
    width: 1200px; height: 1200px; overflow: hidden;
    background: var(--backdrop);
  }
  .letterhead {
    position: absolute; left: 281px; top: 160px;
    width: 638px; height: 829px;
    background: var(--paper);
    border: 1px solid var(--paper-edge);
    font-family: "Arimo", Helvetica, Arial, sans-serif;
    color: var(--ink);
  }
  .brand {
    position: absolute; left: 0; right: 0; top: 58px;
    text-align: center;
    font-family: "Figtree", Arial, sans-serif;
    font-weight: 300; font-size: 17px; letter-spacing: 3px;
    text-transform: uppercase; color: var(--navy);
  }
  .recipient {
    position: absolute; left: 49px; top: 219px;
    font-style: normal; font-size: 11.2px; line-height: 11.4px;
  }
  .salutation {
    position: absolute; left: 51px; top: 305px;
    font-size: 12px; font-weight: 700;
  }
  .body-copy {
    position: absolute; left: 51px; top: 348px; width: 545px;
    font-size: 11px; line-height: 11.4px;
    hyphens: auto;
  }
  .body-copy p + p { margin-top: 11.4px; }
  .sign-off { position: absolute; left: 54px; top: 592px; }
  .sign-off .name { font-size: 13.5px; font-weight: 700; line-height: 16px; text-transform: uppercase; }
  .sign-off .role { font-size: 13px; line-height: 16px; }
  .signature {
    position: absolute; left: 51px; top: 637px;
    width: 97px; height: 50px;
    background: var(--signature); border-radius: 2px;
  }
  .footer-rule {
    position: absolute; left: 47px; top: 756px; width: 550px;
    height: 1px; background: var(--sand);
  }
  .contact-bar {
    position: absolute; left: 57px; top: 767px; width: 530px;
    display: flex; justify-content: space-between; align-items: center;
    font-family: "Figtree", Arial, sans-serif;
    font-size: 8px; letter-spacing: 0.8px; text-transform: uppercase;
    color: var(--ink-soft);
  }
  .contact-bar .web { color: var(--sand); font-weight: 700; }
</style>
</head>
<body>
  <main class="letterhead">
    <div class="brand">Harbourline Estate Group</div>

    <address class="recipient">
      Mr Dorian Welk<br>
      Founder and CEO<br>
      Your Company,<br>
      412 Fernleigh Road, Suite 210<br>
      Halvern, Canada 58213
    </address>

    <div class="salutation">Dear Sir</div>

    <div class="body-copy" lang="la">
      <p>Lorem ipsum dolor sit amet. Non quam iste ut dolor repellendus aut quasi porro nam molestias ullam ut sint ipsa! Qui accusamus assumenda qui quae tempore sit quia velit aut porro tempora. Est iste explicabo aut alias impedit est sequi quis.</p>
      <p>Cum rerum molestiae id galisum odit et autem voluptas aut blanditiis iste ut aspernatur itaque ut tempora laudantium vel voluptatem repudiandae! Ea delectus omnis est voluptas odit ut assumenda quisquam eos facere sunt qui quis vitae. Qui velit dolorem in distinctio</p>
      <p>dignissimos rem voluptatem totam ut quia nostrum cum quas consequuntur. Quo aliquid earum eum optio ducimus qui fugiat veniam qui blanditiis velit ut quos dolores non officiis enim ut voluptatem veritatis.</p>
      <p>At quia sunt nam quibusdam mollitia aut rerum laudantium et inventore molestiae aut cumque consequatur. 33 minima velit rem quasi galisum ut quae magni sed praesentium possimus 33 commodi quam qui quae aperiam est enim accusantium. Sed Quis laboriosam ut suscipit maxime cum reprehenderit adipisci. Non nihil dolor ut obcaecati commodi aut Quis provident eos doloribus cumque.</p>
      <p>At quia sunt nam quibusdam mollitia aut rerum laudantium et inventore molestiae aut cumque consequatur. 33 minima velit rem quasi galisum ut quae</p>
    </div>

    <div class="sign-off">
      <div class="name">Maris Toppel</div>
      <div class="role"><span class="suburb">“Suburb”</span> Specialist – Redlands &amp; Surrounds</div>
    </div>
    <div class="signature" role="img" aria-label="Handwritten signature of Maris Toppel"></div>

    <div class="footer-rule"></div>
    <div class="contact-bar">
      <span class="phone">0417 862 905</span>
      <span class="divider">|</span>
      <span class="email">MT@HarbourlineEstateGroup.com.au</span>
      <span class="divider">|</span>
      <span class="web">www.harbourlineestategroup.com.au</span>
    </div>
  </main>
</body>
</html>
```